Guiding the Evergreen Young Competitor:
A Family Roadmap for Nurturing Bold, Steady, and Resilient Daughters on Fields and Beyond.
📘 Book Cover Design Brief – “Guiding the Evergreen Young Competitor”

Project Title:
Design a bold, inspiring book cover for a best-selling book titled:
Guiding the Evergreen Young Competitor
Subtitle: A Family Roadmap for Nurturing Bold, Steady, and Resilient Daughters on Fields and Beyond

🎯 Audience:

Parents of female athletes ages 14–20 who want their daughters to build confidence, strength, resilience, and long-term success both in sports and in life.

This book should feel encouraging, empowering, and credible — NOT cheesy, childish, or overly academic.

📕 Design Tone & Style:

Powerful and professional — should feel like a best-selling book from a leading performance or parenting expert

Emotionally compelling — conveys hope, resilience, strength, and possibility

Visually modern and clean — avoid anything overly busy, cliché, or childish

Heroic/aspirational tone — think transformation, leadership, strong positioning

💡 Visual Direction / Ideas (Use as Inspiration, Not Limitation):

Strong, confident teenage female athlete imagery — adaptable beyond one specific sport

Symbolic visuals — e.g. athlete standing strong, on a starting line, looking bold into the future, silhouette, or power stance

Bold typography that feels clean and modern (e.g., Proxima Nova, Montserrat, Gotham, Bebas Neue, etc.)

A title that stands out clearly when viewed as a thumbnail on Bookvale

Color tones: Empowering, modern, and strong: think deep blues, greens, purples, or golds — avoid playful pastels or overly girly themes

Potential imagery: textured backgrounds, motion, bravery, development, strength, growth, sport/action overlays

🔥 What the Cover MUST Communicate:

✅ This is for parents who want strong, confident female athletes
✅ It’s a guidebook for personal development AND sports performance
✅ It’s about creating “UNSHAKEABLE” confidence — physically, mentally and emotionally
✅ The message is: You can help your daughter become her strongest, most confident self

📚 Back-of-Book Summary (for context):

"Guiding the Evergreen Young Competitor" is a parent's blueprint to building girls who are strong in body, confident in mind, and ready to lead on and off the field. Through simple strategies around strength training, mindset, nutrition, and character development, this book gives parents the tools to help their daughters stay injury-resistant, break through mental barriers, and unlock their full potential — in sports and in life.

✅ Deliverables:

Full cover design (front, back, spine) for paperback
High-resolution files (print-ready)
Source files (PSD, AI, etc.)
3D mockup versions of the book (standing, flat, stack)

Target Market(s)

Industry/Entity Type

Fitness

Font styles to use
Sans Serif

Colors
FFF300
FFF600
FEFA6F
FFFEC7
FFFEE8

Requirements
Must have
• Bold Font
Should not have
• I don't want an image of a female athlete. I want this to be font based.

```html
<!DOCTYPE html>
<html lang="en">
<head>
<meta charset="utf-8">
<title>Guiding the Evergreen Young Competitor</title>
<link rel="stylesheet" href="https://fonts.googleapis.com/css2?family=Bebas+Neue&family=Oswald:wght@600&display=swap">
<style>
  :root {
    --navy: #1f3577;
    --navy-deep: #172a63;
    --white: #ffffff;
    --gold: #b39d55;
    --gold-light: #ebe2a6;
    --gold-mid: #cdb873;
  }
  * { margin: 0; padding: 0; box-sizing: border-box; }
  html, body { width: 801px; height: 1200px; overflow: hidden; background: var(--navy); }
  .cover {
    position: relative;
    width: 801px;
    height: 1200px;
    overflow: hidden;
    background: radial-gradient(ellipse at 50% 45%, var(--navy) 0%, var(--navy-deep) 100%);
  }
  .cover-texture { position: absolute; inset: 0; width: 100%; height: 100%; }
  .cover-type { position: absolute; inset: 0; width: 100%; height: 100%; }
  .subtitle {
    font-family: "Oswald", "Arial Narrow", sans-serif;
    font-weight: 600;
    font-size: 29px;
    fill: var(--gold-mid);
    letter-spacing: 1px;
  }
  .title {
    font-family: "Bebas Neue", "Oswald", sans-serif;
    fill: var(--white);
  }
  .title-accent { fill: url(#goldSheen); }
  .athlete-art {
    position: absolute;
    left: 174px;
    top: 590px;
    width: 522px;
    height: 520px;
    border-radius: 46% 54% 40% 60% / 50% 40% 60% 50%;
    background: radial-gradient(ellipse at 50% 45%, rgba(179,157,85,0.6) 0%, rgba(179,157,85,0.25) 55%, rgba(179,157,85,0) 75%);
  }
  .imprint {
    position: absolute;
    left: 0;
    right: 0;
    top: 1010px;
    display: flex;
    flex-direction: column;
    align-items: center;
    gap: 14px;
  }
  .imprint-circle {
    width: 94px;
    height: 94px;
    border-radius: 50%;
    border: 3px solid var(--gold);
  }
  .imprint-name {
    font-family: "Bebas Neue", "Oswald", sans-serif;
    font-size: 34px;
    letter-spacing: 3px;
    color: var(--white);
    line-height: 1;
  }
</style>
</head>
<body>
<main class="cover">
  <svg class="cover-texture" viewBox="0 0 801 1200" aria-hidden="true">
    <filter id="paperGrain">
      <feTurbulence type="fractalNoise" baseFrequency="0.9" numOctaves="2" seed="4"/>
      <feColorMatrix values="0 0 0 0 0.35  0 0 0 0 0.45  0 0 0 0 0.85  0 0 0 0.35 0"/>
    </filter>
    <rect width="801" height="1200" filter="url(#paperGrain)"/>
  </svg>

  <svg class="cover-type" viewBox="0 0 801 1200">
    <defs>
      <linearGradient id="goldSheen" x1="0" x2="1" y1="0" y2="0">
        <stop offset="0" stop-color="#b09a50"/>
        <stop offset="0.5" stop-color="#ece3a8"/>
        <stop offset="1" stop-color="#b09a50"/>
      </linearGradient>
    </defs>
    <text class="subtitle" x="400.5" y="79" text-anchor="middle" textLength="654" lengthAdjust="spacingAndGlyphs">A FAMILY ROADMAP FOR NURTURING BOLD, STEADY, AND RESILIENT</text>
    <text class="subtitle" x="400.5" y="113" text-anchor="middle">DAUGHTERS ON FIELDS AND BEYOND</text>

    <text class="title" x="62" y="268" font-size="197" textLength="689" lengthAdjust="spacingAndGlyphs">GUIDING THE</text>
    <text class="title title-accent" x="62" y="406" font-size="174" textLength="689" lengthAdjust="spacingAndGlyphs">EVERGREEN</text>
    <text class="title" x="62" y="641" font-size="317" textLength="689" lengthAdjust="spacingAndGlyphs">YOUNG</text>
    <text class="title" x="62" y="858" font-size="291" textLength="689" lengthAdjust="spacingAndGlyphs">COMPETITOR</text>
  </svg>

  <div class="athlete-art" role="img" aria-label="Gold silhouette of a young female tennis player swinging a racket mid-stride"></div>

  <div class="imprint">
    <div class="imprint-circle"></div>
    <div class="imprint-name">EVERGREEN PRESS</div>
  </div>
</main>
</body>
</html>
```